Construction Plant Hire Business Promotional Flyer

I need a promotional flyer / document folder. So an A4 page flyer that can be printed to make an a4 folder that the sales guy can also put his business card into. most of the equipment that i have is excavators, trucks, vacuum excavators, skidsteer loaders and water trucks and trailers. I can also source other equipment to hire out though so i don't want to limit that details to just that equipment. you can view my current brochure online (i don't really like the brochure or the website) to give an idea on the equipment that i have.

Target Market(s)

Construction Industry that requires plant and equipment hire, civil construction industry,

Industry/Entity Type

Business

Contact Information for Business Card

double sided with matte finish and a solid color on the back with logo in reverse and cards to be cut slightly smaller than standard

Number of Pages Required

4 page

Font styles to use
Sans Serif

Colors
0455a3

Requirements
Must have
• similar to other equipment hire companies. tralvok.com.au, mobrelhire.com.au and pekdarn.com.au
• the company blue color that is on our current website.
• current logo.
• ability to edit website
Nice to have
• photos of construction equipment, simple to read so it does get read when dropped off.
Should not have
• too much text

```html
<!DOCTYPE html>
<html lang="en">
<head>
<meta charset="utf-8">
<title>Equipment Hire Range</title>
<link href="https://fonts.googleapis.com/css2?family=Arimo:wght@400;700&display=swap" rel="stylesheet">
<style>
  :root {
    --row-light: #f3f2f2;
    --row-dark: #e6e5e5;
    --heading-blue: #0b7dc3;
    --brand-blue: #0455a3;
    --wave-blue: #0a7fc8;
    --wave-grey: #cfcfcf;
    --text: #2a2a2a;
  }
  * { margin: 0; padding: 0; box-sizing: border-box; }
  html, body { width: 1200px; height: 849px; overflow: hidden; }
  body { font-family: "Arimo", Arial, sans-serif; color: var(--text); background: var(--row-dark); }
  .sheet { position: relative; width: 1200px; height: 849px; overflow: hidden; }
  .band { position: absolute; left: 0; width: 1200px; }
  .band--light { background: var(--row-light); }
  .band--dark { background: var(--row-dark); }
  .footer-wave { position: absolute; left: 0; top: 0; width: 1200px; height: 849px; }
  .photo {
    position: absolute; width: 236px; height: 160px;
    background: #fff; padding: 5px;
  }
  .photo span { display: block; width: 100%; height: 100%; }
  .photo--yellow span { background: linear-gradient(160deg, #e9eef2 0%, #d8b54a 55%, #6b5a3c 100%); }
  .photo--truck span { background: linear-gradient(160deg, #eef1f4 0%, #c9ced6 55%, #6d7a55 100%); }
  .photo--trailer span { background: linear-gradient(160deg, #ffffff 0%, #3a3a3a 60%, #ffffff 100%); }
  .photo--tank span { background: linear-gradient(160deg, #ffffff 0%, #3fc79a 55%, #9a9a9a 100%); }
  .heading {
    position: absolute; width: 300px; text-align: center;
    color: var(--heading-blue); font-weight: 700; font-size: 16px; line-height: 20px;
  }
  .text { position: absolute; font-size: 12px; line-height: 20px; white-space: nowrap; }
  .center { width: 300px; text-align: center; }
</style>
</head>
<body>
<div class="sheet">
  <div class="band band--light" style="top:0;height:184px"></div>
  <div class="band band--dark" style="top:184px;height:180px"></div>
  <div class="band band--light" style="top:364px;height:180px"></div>

  <svg class="footer-wave" viewBox="0 0 1200 849" aria-hidden="true">
    <defs>
      <linearGradient id="waveRight" x1="0" x2="1" y1="0" y2="0">
        <stop offset="0" stop-color="#0f7fcb"/>
        <stop offset="1" stop-color="#3a9ad6"/>
      </linearGradient>
    </defs>
    <polygon points="0,688 0,726 690,849 760,849" fill="var(--wave-grey)"/>
    <polygon points="980,745 1200,726 1200,849 980,849" fill="var(--wave-grey)"/>
    <polygon points="0,726 0,849 690,849" fill="var(--wave-blue)"/>
    <polygon points="620,849 1200,726 1200,849" fill="url(#waveRight)"/>
  </svg>

  <!-- Row 1 -->
  <div class="photo photo--truck" style="left:22px;top:13px"><span role="img" aria-label="Photo of a hydro vacuum excavation truck"></span></div>
  <div class="heading" style="left:272px;top:22px">VACUUM EXCAVATORS</div>
  <div class="text" style="left:309px;top:64px">Varro Midline<br>3000LTR Spira-Vac Hydro Vac with Boom</div>
  <div class="text" style="left:309px;top:112px">Kestrel Hauler KX-Series<br>3000LTR Hi CFM Hydro Vac</div>

  <div class="heading" style="left:612px;top:20px">EXCAVATORS</div>
  <div class="text" style="left:682px;top:55px">Mini<br>Small<br>Medium<br>Large<br>Low Drill</div>
  <div class="text" style="left:799px;top:56px">1.7T - 5.5T<br>8.0T - 14T<br>20T - 30T<br>35T - 75T<br>20T - 30T</div>
  <div class="photo photo--yellow" style="left:944px;top:13px"><span role="img" aria-label="Photo of a tracked excavator on site"></span></div>

  <!-- Row 2 -->
  <div class="photo photo--yellow" style="left:22px;top:194px"><span role="img" aria-label="Photo of a motor grader"></span></div>
  <div class="heading" style="left:271px;top:214px">GRADERS</div>
  <div class="text center" style="left:270px;top:248px">GR-210, GR-230<br>GR-250, GR-270</div>

  <div class="heading" style="left:612px;top:214px">TIPPERS</div>
  <div class="text center" style="left:612px;top:246px">3M - 10M Tippers<br>Truck &amp; Dog<br>Semi Tipper<br>Single &amp; Triple Axel Tag Trailers</div>
  <div class="photo photo--truck" style="left:944px;top:194px"><span role="img" aria-label="Photo of a tipper truck with tag trailer"></span></div>

  <!-- Row 3 -->
  <div class="photo photo--yellow" style="left:22px;top:374px"><span role="img" aria-label="Photo of a pad foot compaction roller"></span></div>
  <div class="heading" style="left:271px;top:396px">COMPACTION</div>
  <div class="text" style="left:318px;top:446px">1.3T - 8T<br>12T - 20T<br>5T - 20T</div>
  <div class="text" style="left:440px;top:446px">Twin Drum Roller<br>Smooth Drum Roller<br>Pad Foot Roller</div>

  <div class="heading" style="left:612px;top:396px">SKID STEERS</div>
  <div class="text center" style="left:612px;top:434px">Torvan Loader SL-A<br>Torvan Loader SL-B High Flow<br>Open and Closed<br>Cab Models Available</div>
  <div class="photo photo--yellow" style="left:944px;top:374px"><span role="img" aria-label="Photo of a skid steer loader with bucket"></span></div>

  <!-- Row 4 -->
  <div class="photo photo--trailer" style="left:22px;top:556px"><span role="img" aria-label="Photo of a fuel tank trailer"></span></div>
  <div class="heading" style="left:273px;top:577px">SMALL EQUIPMENT</div>
  <div class="text center" style="left:268px;top:621px;line-height:24px">Generators<br>Compressors<br>Fuel Trailers</div>

  <div class="heading" style="left:610px;top:577px">WATER CARTAGE</div>
  <div class="text" style="left:665px;top:622px;line-height:24px">1500 LTR<br>7000 - 45 000 LTR<br>7000 LTR</div>
  <div class="text" style="left:798px;top:622px;line-height:24px">Water Trailer<br>Water Trucks<br>Water Skid</div>
  <div class="photo photo--tank" style="left:944px;top:556px"><span role="img" aria-label="Photo of a water tank skid with pump"></span></div>
</div>
</body>
</html>
```